It is a leisure sector investment company.The company plans to invest in a luxurious 5 star resort

We need a stationery design to our company 'Copper Lantern Limited' using the winning logo design. We need the letter heads, envelopes & the business cards. Should be simple, plain and professional
We have upload the source file & vector files which gives our logo design. We prefer the bottom logo.

Have updated under 'must have priorities', the company name, address, tel no. fax no. & the company reg no. which should come on the letter head. the long envelope should have the company name, tel & fax no. 
Business card should have the company name, name on the card, designation, tel no. fax no.  

- Letter head details:
Copper Lantern Limited
14 Floor, South Wing, Halvard Merchant Plaza,
Merrow Court, Colombo 01, Sri Lanka
Tel: +94 11 5047293 Fax: +94 11 5047298
Company Reg No.QX 6142
Long Envelope should have only the company name, adress, Tel & Fax
Business Cards should have the company name, Tel & Fax:
Business Card 1 - Lasantha Gunaratne - Chairman
Business Card 2 - Nimal.T.Wijesooriya - COO

```html
<!DOCTYPE html>
<html lang="en">
<head>
<meta charset="utf-8">
<title>Copper Lantern Limited – Long Envelope</title>
<link rel="stylesheet" href="https://fonts.googleapis.com/css2?family=Arimo:wght@400&family=Cinzel:wght@400&display=swap">
<style>
  :root {
    --ink: #4b3f3b;
    --paper: #ffffff;
    --flourish: #efeeed;
    --flourish-soft: #f6f5f4;
  }
  html, body {
    margin: 0;
    padding: 0;
    width: 1200px;
    height: 521px;
    overflow: hidden;
    background: var(--paper);
  }
  .envelope {
    position: relative;
    width: 1200px;
    height: 521px;
    background: var(--paper);
    font-family: "Arimo", "Helvetica Neue", Arial, sans-serif;
    color: var(--ink);
  }
  .sender {
    position: absolute;
    left: 30px;
    top: 38px;
    width: 360px;
    text-align: center;
  }
  .brand-mark {
    display: block;
    width: 46px;
    height: 46px;
    margin: 0 auto;
    border-radius: 50%;
    background: var(--ink);
  }
  .company-name {
    margin: 12px 0 0;
    font-family: "Cinzel", "Trajan Pro", Georgia, serif;
    font-weight: 400;
    color: var(--ink);
    line-height: 1;
  }
  .company-name__main {
    display: block;
    font-size: 34px;
    letter-spacing: 0.01em;
    white-space: nowrap;
  }
  .company-name__suffix {
    display: block;
    margin-top: 6px;
    font-size: 17px;
    letter-spacing: 0.34em;
    padding-left: 0.34em;
    text-transform: uppercase;
  }
  .address {
    margin: 24px 0 0;
    font-style: normal;
    font-size: 14.5px;
    line-height: 20.5px;
    white-space: nowrap;
  }
  .address .divider {
    padding: 0 3px;
  }
  .flourish-area {
    position: absolute;
    left: 745px;
    top: 195px;
    width: 455px;
    height: 326px;
    border-top-left-radius: 180px 160px;
    background: linear-gradient(135deg, var(--flourish-soft) 0%, var(--flourish) 45%, var(--flourish) 100%);
  }
</style>
</head>
<body>
  <main class="envelope">
    <section class="sender">
      <span class="brand-mark" aria-hidden="true"></span>
      <h1 class="company-name">
        <span class="company-name__main">Copper Lantern</span>
        <span class="company-name__suffix">Limited</span>
      </h1>
      <address class="address">
        14 Floor, South Wing, Halvard Merchant Plaza,<br>
        Merrow Court, Colombo 01, Sri Lanka<br>
        Tel: +94 11 5047293<span class="divider">|</span>Fax: +94 11 5047298
      </address>
    </section>
    <div class="flourish-area" role="img" aria-label="Large faint ornamental flourish decoration in light grey"></div>
  </main>
</body>
</html>
```